New Chiropractic Office needs a fresh flyer design!

We need a flyer design for our chiropractic office for our hometown based chiropractic office called "Corliss Chiropractic" Dr. Martin Corliss provides chiropractic services including adjustments, xrays and wellness exercises with a fresh approach to chiropractic which focuses on getting your body aligned correctly to be a better you. We dont like to focus on coming in just for pain although that is what most people associate our operation with so we understand that comes with the territory. However we would like our flyers to express health and wellness rather than medical or pain. We would like our flyer to emphasize our "New Patient Special" which includes consultation, exam, xrays and first treatment for only $50. We also accept most insurance plans. Call for an appointment 608-371-5829.

Industry/Entity Type

Office

```html
<!DOCTYPE html>
<html lang="en">
<head>
<meta charset="utf-8">
<title>Corliss Chiropractic – New Patient Special</title>
<link rel="stylesheet" href="https://fonts.googleapis.com/css2?family=Roboto+Condensed:wght@700&family=Arimo:wght@400;700&display=swap">
<style>
  :root {
    --backdrop: #2b2b2b;
    --paper: #ffffff;
    --olive: #6f7f2f;
    --olive-dark: #5c6b26;
    --lime: #9cc33a;
    --yellow: #f6ee00;
    --ink: #444444;
    --ink-soft: #666666;
    --brand-grey: #6a6a6a;
    --photo-light: #d9e6f2;
    --photo-mid: #8fb0cf;
  }
  * { margin: 0; padding: 0; box-sizing: border-box; }
  html, body { width: 1200px; height: 1000px; overflow: hidden; }
  body { background: var(--backdrop); position: relative; font-family: "Arimo", Arial, sans-serif; }

  .flyer {
    position: absolute; left: 267px; top: 70px;
    width: 666px; height: 860px;
    background: var(--paper); overflow: hidden;
  }
  .band { position: absolute; left: 0; top: 0; width: 666px; height: 860px; }

  .brand { position: absolute; left: 40px; top: 40px; display: flex; align-items: center; gap: 16px; }
  .brand-dot { width: 48px; height: 48px; border-radius: 50%; background: var(--lime); flex: none; }
  .brand-name {
    font-family: "Arimo", Arial, sans-serif; font-weight: 700;
    font-size: 36px; letter-spacing: 0.5px; color: var(--brand-grey); white-space: nowrap;
  }

  .intro {
    position: absolute; left: 40px; top: 126px; width: 260px;
    font-size: 12.5px; line-height: 16px; color: var(--ink-soft);
  }

  .photo {
    position: absolute; left: 323px; top: 118px; width: 343px; height: 592px;
    background: radial-gradient(ellipse at 55% 45%, var(--photo-light) 0%, var(--photo-mid) 55%, rgba(143,176,207,0) 75%);
  }

  .headline {
    position: absolute; left: 38px; top: 280px;
    font-family: "Roboto Condensed", "Arial Narrow", sans-serif; font-weight: 700;
    font-size: 92px; line-height: 75px; letter-spacing: -3px;
    color: var(--yellow); text-transform: uppercase;
    text-shadow: 2px 3px 4px rgba(0,0,0,0.35);
  }
  .offer {
    position: absolute; left: 40px; top: 515px; width: 300px;
    font-size: 20px; line-height: 25px; color: #fff;
  }
  .offer p + p { margin-top: 12px; }

  .address {
    position: absolute; left: 40px; top: 766px;
    font-size: 20px; line-height: 26px; color: var(--ink);
  }
  .divider { position: absolute; left: 225px; top: 742px; width: 1px; height: 74px; background: var(--ink); }
  .call { position: absolute; left: 253px; top: 730px; }
  .call-label { font-size: 31px; color: var(--ink); line-height: 36px; }
  .call-phone { font-size: 58px; font-weight: 700; color: var(--olive-dark); line-height: 64px; letter-spacing: -0.5px; }
</style>
</head>
<body>
  <main class="flyer">
    <svg class="band" viewBox="0 0 666 860" aria-hidden="true">
      <path d="M0 248 C 160 225, 320 222, 666 262 L 666 700 C 420 640, 200 660, 0 735 Z" fill="var(--lime)"/>
      <path d="M0 262 C 160 240, 320 238, 666 280 L 666 690 C 420 630, 200 648, 0 720 Z" fill="var(--olive)"/>
    </svg>

    <div class="photo" role="img" aria-label="Photo of a man seen from behind holding his upper and lower back"></div>

    <div class="brand">
      <span class="brand-dot"></span>
      <span class="brand-name">CORLISS CHIROPRACTIC</span>
    </div>

    <p class="intro">Dr. Martin Corliss provides chiropractic services including adjustments, xrays and wellness exercises with a fresh approach to chiropractic which focuses on getting your body aligned correctly to be a better you.</p>

    <h1 class="headline">New<br>Patient<br>Special</h1>

    <div class="offer">
      <p>includes consultation,<br>exam, xrays and first<br>treatment for only $50.</p>
      <p>We also accept<br>most insurance plans.</p>
    </div>

    <p class="address">18342 Larkspur,<br>Dunmore MI 48277</p>
    <span class="divider"></span>
    <div class="call">
      <p class="call-label">Call for an appointment</p>
      <p class="call-phone">608-371-5829</p>
    </div>
  </main>
</body>
</html>
```